Velvet Meadow Custom Handmade Designs and more needs new business card

I am looking to get a new design for my business cards. My business is based in Baltimore, MD. The company is called “Velvet Meadow”. We offers a variety of products and services. The products include handmade earrings, phone cases, picture frame, hats, tutu’s, ect. You name it we make it. As well as a lipstick line called “Jinxa”. We also are a independent consultant for Lorna Belt and Odette Brim. Lastly, we offer make up services from our certified MUA. I know it seems like a lot but it works. It’s all thinks girly. Our company tag lines are “You name it, we make it!” and “Everyday is a fashion show and the world id your runway… are you ready?”. I would like the business cards to have a girly appeal to it. I would like it to have some sample pictures of what we do if possible. I am open to different ideas. If you want to see what we have, you can view my website. MyVelvetMeadow.com …. its not finished but it will give you an idea of everything. I have attached my new designed logos. There are 3 different types that you can choose from. If you need pictures, let me know of what. Thanks!

Target Market(s)

Wide market women of all ages

Industry/Entity Type

Business

Contact Information for Business Card

Name: Velvet Meadow ; Website: MyVelvetMeadow.com ; Number: 555-204-1938 ; Email: MyVelvetMdw@mailnest.net ; IG: Velvet_Mdw Pagebook.net/VelvetMeadow14 ; Craftly.net/Shop/MyVelvetMeadow

Font styles to use
Serif
Sans Serif
Decorative
Script

Requirements
Must have
• One of the logos (but you can change the colors if you like)
Nice to have
• Location: Linden Hollow, MD ; Owner/ designer: Bianca Thorne ; Taglines: You Name it, we make it and/or Every day is a fashion show and the world is your runway… Are you ready?

```html
<!DOCTYPE html>
<html lang="en">
<head>
<meta charset="utf-8">
<title>Velvet Meadow – Business Card</title>
<link href="https://fonts.googleapis.com/css2?family=Oleo+Script:wght@700&family=Patrick+Hand&family=Open+Sans:wght@400;700&display=swap" rel="stylesheet">
<style>
  :root {
    --pink: #d6147f;
    --paper: #f7f7f7;
    --ink: #333333;
    --muted: #555555;
    --row: #ececec;
    --tag-ink: #3a1030;
    --backdrop: #e9e4dc;
  }
  * { box-sizing: border-box; margin: 0; padding: 0; }
  html, body { width: 1200px; height: 902px; overflow: hidden; }
  body { background: var(--backdrop); font-family: "Open Sans", sans-serif; position: relative; }

  .card {
    position: absolute; top: 150px; width: 340px; height: 595px;
    background: var(--paper); overflow: hidden;
    box-shadow: 0 6px 18px rgba(0,0,0,.18);
  }
  .card--front { left: 200px; }
  .card--back { left: 660px; }

  /* front */
  .brand-lockup {
    position: absolute; left: 0; right: 0; top: 200px;
    display: flex; align-items: center; justify-content: center; gap: 12px;
  }
  .brand-mark { width: 22px; height: 22px; background: var(--pink); flex: none; }
  .brand-name {
    font-family: "Open Sans", sans-serif; font-weight: 700; font-size: 34px;
    color: var(--pink); line-height: 1;
  }
  .tagline-band {
    position: absolute; left: 0; right: 0; top: 262px; padding: 10px 22px;
    background: var(--pink);
    font-family: "Patrick Hand", cursive; font-size: 20px; line-height: 1.15;
    color: var(--tag-ink); text-align: center;
  }
  .shop-url {
    position: absolute; left: 0; right: 0; top: 340px; text-align: center;
    font-weight: 700; font-size: 12.5px; color: var(--ink); letter-spacing: .2px;
  }
  .edge-tab { position: absolute; width: 10px; height: 60px; background: var(--pink); }
  .edge-tab--top { left: 0; top: 0; }
  .edge-tab--bottom { right: 0; bottom: 0; }

  /* back */
  .back-strip { position: absolute; left: 0; top: 0; width: 26px; height: 175px; background: var(--pink); }
  .name-banner {
    position: absolute; right: 0; top: 42px; width: 270px; height: 46px;
    background: var(--pink); color: #fff; text-align: center;
    font-family: "Oleo Script", cursive; font-weight: 700; font-size: 30px; line-height: 46px;
  }
  .role { position: absolute; right: 60px; top: 94px; font-size: 14px; color: var(--muted); }
  .mini-lockup {
    position: absolute; left: 40px; top: 120px;
    display: flex; align-items: center; gap: 8px;
  }
  .mini-mark { width: 14px; height: 14px; background: var(--pink); flex: none; }
  .mini-brand {
    font-family: "Open Sans", sans-serif; font-weight: 700; font-size: 22px;
    color: var(--pink); line-height: 1;
  }
  .mini-tagline {
    position: absolute; left: 40px; top: 150px; width: 260px;
    font-family: "Patrick Hand", cursive; font-size: 12px; line-height: 1.1; color: var(--tag-ink);
  }
  .contact-list { position: absolute; left: 22px; right: 22px; top: 200px; list-style: none; }
  .contact-item {
    display: flex; align-items: center; gap: 14px; height: 36px; margin-bottom: 12px;
    font-size: 15px; color: var(--muted);
  }
  .contact-item span { flex: 1; padding: 6px 8px; }
  .contact-item:nth-child(even) span { background: var(--row); }
  .contact-icon { width: 16px; height: 16px; flex: none; }
  .back-foot { position: absolute; left: 0; bottom: 0; width: 70px; height: 70px; background: var(--pink); }
</style>
</head>
<body>

<section class="card card--front" aria-label="Card front">
  <div class="brand-lockup">
    <span class="brand-mark"></span>
    <span class="brand-name">Velvet Meadow</span>
  </div>
  <p class="tagline-band">Every day is a style moment and the street is your stage... Ready to shine?</p>
  <p class="shop-url">CRAFTLY.NET/SHOP/MYVELVETMEADOW</p>
  <div class="edge-tab edge-tab--top"></div>
  <div class="edge-tab edge-tab--bottom"></div>
</section>

<section class="card card--back" aria-label="Card back">
  <div class="back-strip"></div>
  <div class="name-banner">Bianca Thorne</div>
  <p class="role">MD / Owner</p>
  <div class="mini-lockup">
    <span class="mini-mark"></span>
    <span class="mini-brand">Velvet Meadow</span>
  </div>
  <p class="mini-tagline">Every day is a style moment and the street is your stage... Ready to shine?</p>

  <ul class="contact-list">
    <li class="contact-item">
      <svg class="contact-icon" viewBox="0 0 16 16"><path d="M8 1a5 5 0 0 0-5 5c0 4 5 9 5 9s5-5 5-9a5 5 0 0 0-5-5z" fill="none" stroke="#d6147f" stroke-width="1.6"/><circle cx="8" cy="6" r="1.8" fill="#d6147f"/></svg>
      <span>Lantern Blvd, Linden Hollow</span>
    </li>
    <li class="contact-item">
      <svg class="contact-icon" viewBox="0 0 16 16"><path d="M4 1l3 3-2 2c1 2 2 3 4 4l2-2 3 3-2 2C6 13 3 10 2 3z" fill="#d6147f"/></svg>
      <span>555-204-1938</span>
    </li>
    <li class="contact-item">
      <svg class="contact-icon" viewBox="0 0 16 16"><rect x="1.5" y="3.5" width="13" height="9" fill="none" stroke="#d6147f" stroke-width="1.4"/><path d="M2 4l6 5 6-5" fill="none" stroke="#d6147f" stroke-width="1.4"/></svg>
      <span>MyVelvetMdw@mailnest.net</span>
    </li>
    <li class="contact-item">
      <svg class="contact-icon" viewBox="0 0 16 16"><circle cx="8" cy="8" r="6.5" fill="none" stroke="#d6147f" stroke-width="1.4"/><path d="M1.5 8h13M8 1.5c-3 3-3 10 0 13M8 1.5c3 3 3 10 0 13" fill="none" stroke="#d6147f" stroke-width="1"/></svg>
      <span>MyVelvetMeadow.com</span>
    </li>
    <li class="contact-item">
      <svg class="contact-icon" viewBox="0 0 16 16"><rect x="2" y="2" width="12" height="12" fill="#d6147f"/></svg>
      <span>VELVET_MDW</span>
    </li>
    <li class="contact-item">
      <svg class="contact-icon" viewBox="0 0 16 16"><circle cx="8" cy="8" r="6" fill="#d6147f"/></svg>
      <span>VELVETMEADOW</span>
    </li>
  </ul>
  <div class="back-foot"></div>
</section>

</body>
</html>
```